Need help in designing new business card utilizing our new logo.

Veltrix Solutions works with Construction Business Owners, Managers & IT Professionals to strengthen software usage and increase user productivity.

Our Construction Accounting and Mobile Field Management Software Clients engage with us in the following areas:

New Software Implementations
Software Re-Implementations
Redesigning Software Usage at the User Level
Project Coordination & Management
Continued Software Support

Old tag line:
Weighing Options - Implementing Solutions

www.veltrix-solutions.example

Quad Shift is a product, but not needed for a new business card.

```html
<!DOCTYPE html>
<html lang="en">
<head>
<meta charset="utf-8">
<title>Veltrix Solutions – Business Cards</title>
<link rel="stylesheet" href="https://fonts.googleapis.com/css2?family=Arimo:wght@400;700&family=Montserrat:wght@400;600&display=swap">
<style>
  :root {
    --brand-blue: #2e3a97;
    --brand-grey: #c3c4c8;
    --text-grey: #9a9ba0;
    --card-white: #ffffff;
    --backdrop: #2b2b2d;
  }
  * { box-sizing: border-box; margin: 0; padding: 0; }
  html, body { width: 1200px; height: 880px; overflow: hidden; background: var(--backdrop); }
  .canvas { position: relative; width: 1200px; height: 880px; }

  .card {
    position: absolute;
    width: 590px; height: 337px;
    background: var(--card-white);
    border-radius: 22px;
    overflow: hidden;
    font-family: "Arimo", Arial, sans-serif;
  }
  .card--services { left: 50px; top: 70px; }
  .card--contact { left: 560px; top: 473px; }

  .wordmark { color: var(--brand-blue); }
  .wordmark__name {
    font-family: "Montserrat", sans-serif;
    font-weight: 600;
    letter-spacing: 1px;
    line-height: 1;
  }
  .wordmark__sub {
    font-family: "Montserrat", sans-serif;
    font-weight: 400;
    color: var(--text-grey);
    line-height: 1;
  }

  /* Services card */
  .card--services .wordmark { position: absolute; left: 44px; top: 44px; }
  .card--services .wordmark__name { font-size: 42px; }
  .card--services .wordmark__sub { font-size: 13px; letter-spacing: 14.5px; margin-top: 4px; }

  .service-list {
    position: absolute; left: 52px; top: 138px;
    list-style: none;
    color: var(--brand-blue);
    font-size: 16px; font-weight: 700;
  }
  .service-list li { display: flex; align-items: center; margin-bottom: 8px; white-space: nowrap; }
  .service-list li::before {
    content: ""; width: 8px; height: 8px; border-radius: 50%;
    background: var(--brand-blue); margin-right: 12px; flex: none;
  }

  .site-band {
    position: absolute; left: 0; bottom: 22px;
    width: 430px; height: 36px;
    background: var(--brand-blue);
    clip-path: polygon(0 0, 100% 0, 94% 100%, 0 100%);
    color: var(--card-white);
    font-size: 16px; font-weight: 700;
    padding: 9px 0 0 48px;
  }
  .accent-block {
    position: absolute; right: 40px; top: 28px;
    width: 140px; height: 140px;
    background: var(--brand-blue);
  }

  /* Contact card */
  .card--contact .wave { position: absolute; inset: 0; }
  .card--contact .wordmark {
    position: absolute; left: 36px; top: 62px;
    display: flex; align-items: center;
  }
  .wordmark__mark { width: 42px; height: 42px; background: var(--brand-blue); margin-right: 16px; }
  .wordmark__divider { width: 2px; height: 80px; background: var(--brand-blue); margin-right: 14px; }
  .card--contact .wordmark__name { font-size: 34px; }
  .card--contact .wordmark__sub { font-size: 11px; letter-spacing: 9px; margin-top: 5px; }

  .person { position: absolute; right: 34px; top: 22px; text-align: right; }
  .person__name { color: var(--brand-blue); font-size: 20px; font-weight: 700; }
  .person__role { color: var(--text-grey); font-size: 12px; margin-top: 1px; }

  .contact-list {
    position: absolute; right: 22px; top: 130px;
    list-style: none; text-align: right;
    color: var(--card-white); font-size: 13px; line-height: 21px;
  }
  .contact-list li { display: flex; justify-content: flex-end; align-items: center; gap: 7px; white-space: nowrap; }
  .contact-list .contact-email { font-size: 12.5px; }
  .contact-icon { width: 15px; height: 15px; flex: none; }
</style>
</head>
<body>
<main class="canvas">

  <section class="card card--services" aria-label="Services side">
    <div class="accent-block" aria-hidden="true"></div>
    <div class="wordmark">
      <div class="wordmark__name">VELTRIX</div>
      <div class="wordmark__sub">SOLUTIONS</div>
    </div>
    <ul class="service-list">
      <li>New Software Implementations</li>
      <li>Software Re-Implementations</li>
      <li>Redesigning Software Usage at the User Level</li>
      <li>Project Coordination &amp; Management</li>
      <li>Continued Software Support</li>
    </ul>
    <div class="site-band">www.veltrix-solutions.example</div>
  </section>

  <section class="card card--contact" aria-label="Contact side">
    <svg class="wave" viewBox="0 0 590 337" aria-hidden="true">
      <path d="M0 305 C110 304 180 288 215 232 C240 190 265 150 300 118 C285 160 265 200 248 240 C215 295 120 314 0 315 Z" fill="var(--brand-grey)"/>
      <path d="M0 337 L0 318 C120 318 200 300 240 240 C280 170 340 100 450 80 C500 74 550 72 590 72 L590 337 Z" fill="var(--brand-blue)"/>
      <path d="M120 326 C190 323 235 302 254 258" fill="none" stroke="var(--card-white)" stroke-width="2.5"/>
    </svg>

    <div class="wordmark">
      <div class="wordmark__mark" aria-hidden="true"></div>
      <div class="wordmark__divider" aria-hidden="true"></div>
      <div>
        <div class="wordmark__name">VELTRIX</div>
        <div class="wordmark__sub">SOLUTIONS</div>
      </div>
    </div>

    <div class="person">
      <div class="person__name">Dana R. Whitfield</div>
      <div class="person__role">Owner</div>
    </div>

    <ul class="contact-list">
      <li>48B Harbor Lane - PMB 117</li>
      <li>Millbrook NY 12545</li>
      <li>866-555-0142 ext.100
        <svg class="contact-icon" viewBox="0 0 16 16" aria-label="Phone"><circle cx="8" cy="8" r="7" fill="none" stroke="#fff" stroke-width="1.3"/><path d="M5.5 4.5 L7 6 L6.2 7 C6.8 8.3 7.7 9.2 9 9.8 L10 9 L11.5 10.5 L10.6 11.5 C7.6 11 5 8.4 4.5 5.4 Z" fill="#fff"/></svg>
      </li>
      <li>518-555-0193
        <svg class="contact-icon" viewBox="0 0 16 16" aria-label="Mobile"><circle cx="8" cy="8" r="7" fill="none" stroke="#fff" stroke-width="1.3"/><rect x="5.5" y="3.8" width="5" height="8.4" rx="1" fill="none" stroke="#fff" stroke-width="1.2"/></svg>
      </li>
      <li class="contact-email">dana.whitfield@veltrix-solutions.example
        <svg class="contact-icon" viewBox="0 0 16 16" aria-label="Email"><circle cx="8" cy="8" r="7" fill="#fff"/><rect x="4" y="5.3" width="8" height="5.6" fill="var(--brand-blue)"/><path d="M4 5.3 L8 8.6 L12 5.3" fill="none" stroke="#fff" stroke-width="1"/></svg>
      </li>
    </ul>
  </section>

</main>
</body>
</html>
```